Web Design Project

Hi, we need a new and professional design for our company "partnerlinkhubgroup". The website should communicate business but with a friendly and professional touch.

You can use the following categories for the menu;

Home - customer groups - products - voucher system- contact

Give it your best,

Regards,
Dorian

Industry/Entity Type

Business

```html
<!DOCTYPE html>
<html lang="en">
<head>
<meta charset="utf-8">
<title>partnerlinkhubgroup – Business Partners</title>
<link rel="stylesheet" href="https://fonts.googleapis.com/css2?family=PT+Sans:wght@400;700&family=Roboto+Condensed:wght@300;400;700&display=swap">
<style>
  :root {
    --page-bg: #e4e1d8;
    --page-bg-light: #eeece5;
    --panel: #ffffff;
    --navy: #061a7a;
    --blue-deep: #0b2fb0;
    --blue-bright: #2a8df0;
    --badge-blue: #1560d6;
    --ink: #3a3a3a;
    --ink-soft: #555555;
    --muted: #8a8a8a;
    --link: #1f5fb8;
    --date-blue: #2a7fcf;
    --tab-top: #f6f5f1;
    --tab-bottom: #e3e1da;
    --contact-bg: #c9c19d;
    --contact-ink: #4e4834;
    --rule: #b9b9b9;
  }
  * { box-sizing: border-box; margin: 0; padding: 0; }
  html, body { width: 1200px; height: 1128px; overflow: hidden; }
  body {
    background: radial-gradient(ellipse at 40% 30%, var(--page-bg-light), var(--page-bg) 70%);
    font-family: "PT Sans", Tahoma, sans-serif;
    color: var(--ink-soft);
    position: relative;
  }
  .canvas { position: relative; width: 1200px; height: 1128px; }

  .clock { position: absolute; left: 86px; top: 70px; font-size: 15px; color: #7a7a72; }
  .clock b { color: #555; margin-right: 4px; }
  .clock .time { margin-left: 16px; font-weight: 700; color: #555; font-size: 16px; }

  .main-panel {
    position: absolute; left: 345px; top: 36px; width: 836px; height: 1018px;
    background: var(--panel); border-radius: 9px;
    box-shadow: 0 3px 10px rgba(0,0,0,0.18);
  }

  .toolbar { position: absolute; left: 395px; top: 64px; display: flex; align-items: center; }
  .toolbar .tool { width: 24px; height: 24px; display: flex; align-items: center; justify-content: center; }
  .toolbar .sep { width: 1px; height: 28px; background: #cfcfcf; margin: 0 34px; }

  .banner {
    position: absolute; left: 19px; top: 114px; width: 1162px; height: 188px;
    border-radius: 8px 0 0 8px; overflow: hidden;
    background:
      radial-gradient(ellipse 360px 190px at 690px 90px, rgba(90,190,255,0.75), transparent 70%),
      linear-gradient(90deg, var(--navy) 0%, var(--blue-deep) 28%, var(--blue-bright) 55%, var(--blue-deep) 78%, var(--navy) 100%);
    box-shadow: 0 3px 6px rgba(0,0,0,0.25);
  }
  .brand {
    position: absolute; left: 16px; top: 62px;
    font-family: "PT Sans", Tahoma, sans-serif; font-weight: 700; font-size: 30px;
    color: #ffffff; display: flex; align-items: center; gap: 10px;
  }
  .brand .mark { width: 14px; height: 14px; border-radius: 50%; background: #ffffff; }
  .banner-visual {
    position: absolute; left: 401px; top: 35px; width: 188px; height: 149px;
    background: linear-gradient(160deg, #5c6470, #1c2128 70%);
    border-radius: 6px;
  }
  .tagline {
    position: absolute; left: 717px; top: 39px; width: 445px; height: 105px;
    background: linear-gradient(180deg, #1d6fe0, var(--badge-blue));
    border: 1px solid rgba(255,255,255,0.45); border-right: none;
    border-radius: 4px 0 0 4px;
    padding: 14px 0 0 26px; color: #fff;
    font-family: "Roboto Condensed", "Arial Narrow", sans-serif;
  }
  .tagline .big { font-size: 44px; font-weight: 300; letter-spacing: 1px; line-height: 44px; }
  .tagline .small { font-size: 25px; font-weight: 300; letter-spacing: 0.5px; line-height: 30px; }
  .tag-visual {
    position: absolute; left: 1050px; top: 0; width: 112px; height: 140px;
    background: linear-gradient(180deg, rgba(230,236,245,0.0), rgba(230,236,245,0.85) 55%);
    border-radius: 0 0 10px 10px;
  }

  .side-nav { position: absolute; left: 34px; top: 312px; width: 311px; list-style: none; }
  .side-nav li {
    height: 78px; margin-bottom: 10px; padding: 16px 0 0 32px;
    background: linear-gradient(180deg, var(--tab-top), var(--tab-bottom));
    border-radius: 5px 0 0 5px;
    box-shadow: 0 2px 3px rgba(0,0,0,0.12), inset 0 1px 0 #fff;
  }
  .side-nav .label {
    display: block; font-family: "Roboto Condensed", "Arial Narrow", sans-serif;
    font-size: 22px; font-weight: 700; color: #3b3b3b; line-height: 24px; letter-spacing: -0.3px;
  }
  .side-nav .hint { display: block; font-size: 16px; color: var(--muted); line-height: 17px; }

  .primary-contact {
    position: absolute; left: 34px; top: 849px; width: 311px; height: 157px;
    background: var(--contact-bg); border-radius: 8px 0 0 8px;
    padding: 14px 0 0 46px; color: var(--contact-ink); font-size: 17px; line-height: 21px;
  }
  .primary-contact h3 {
    font-family: "Roboto Condensed", "Arial Narrow", sans-serif; font-weight: 400;
    font-size: 27px; line-height: 32px; color: #5a543f; margin-bottom: 6px;
  }
  .primary-contact strong { font-weight: 700; }

  .photo { position: absolute; border-radius: 7px; border: 1px solid #9a9a9a; }
  .photo-welcome { left: 393px; top: 382px; width: 209px; height: 173px;
    background: linear-gradient(135deg, #e6ddd0, #c9b7a0 55%, #f0ece6); }
  .photo-news-1 { left: 794px; top: 725px; width: 130px; height: 90px;
    background: linear-gradient(135deg, #6e5a48, #b99a80 50%, #3d342c); }
  .photo-news-2 { left: 794px; top: 882px; width: 130px; height: 89px;
    background: linear-gradient(135deg, #7c96b0, #d8cbbd 50%, #5d7890); }

  .heading {
    position: absolute; font-family: "Roboto Condensed", "Arial Narrow", sans-serif;
    font-weight: 700; font-size: 31px; line-height: 32px; color: #333; letter-spacing: -0.6px;
  }
  .heading small {
    display: block; font-weight: 400; font-size: 18px; line-height: 22px; color: var(--muted); letter-spacing: 0;
  }
  .welcome-title { left: 631px; top: 376px; }
  .priority-title { left: 393px; top: 628px; width: 335px; padding-bottom: 10px; border-bottom: 1px solid var(--rule); }
  .news-title { left: 794px; top: 628px; }

  .copy { position: absolute; font-size: 16.5px; line-height: 20.5px; color: var(--ink-soft); }
  .welcome-copy { left: 631px; top: 452px; width: 490px; }
  .priority-copy { left: 393px; top: 720px; width: 340px; }

  .more { position: absolute; font-size: 16.5px; color: var(--link); }
  .more::before { content: "|"; color: #aaa; margin-right: 4px; }
  .more::after { content: "|"; color: #aaa; margin-left: 3px; }
  .more .dot { color: #8aa; font-size: 11px; margin-right: 4px; vertical-align: 2px; }
  .more-welcome { right: 71px; top: 562px; }
  .more-news-1 { right: 70px; top: 814px; }
  .more-news-2 { right: 70px; top: 969px; }

  .priority-links { position: absolute; left: 393px; top: 842px; width: 335px; list-style: none; }
  .priority-links li {
    height: 28.5px; padding: 3px 0 0 17px; font-size: 16.5px; color: var(--link);
    border-bottom: 1px dotted #9aa4b4; position: relative;
  }
  .priority-links li::before {
    content: ""; position: absolute; left: 17px; top: 12px; width: 4px; height: 4px; background: #8a9aaa;
  }
  .priority-links li span { margin-left: 14px; }

  .column-rule { position: absolute; left: 761px; top: 616px; width: 1px; height: 368px; background: #9a9a9a; }

  .news-item { position: absolute; left: 945px; width: 190px; font-size: 16.5px; line-height: 20px; color: var(--ink-soft); }
  .news-item .date { color: var(--date-blue); font-weight: 700; font-size: 20px; margin-right: 6px; }
  .news-1 { top: 720px; }
  .news-2 { top: 876px; }
  .news-divider { position: absolute; left: 794px; top: 866px; width: 337px; border-top: 1px dotted #888; }

  .footer { position: absolute; left: 345px; top: 1069px; width: 660px; text-align: center; font-size: 17px; color: #444; }
</style>
</head>
<body>
<div class="canvas">

  <div class="clock"><b>FRI</b>00.00.2013 <span class="time">5:45 PM</span></div>

  <div class="main-panel"></div>

  <nav class="toolbar" aria-label="Quick links">
    <span class="tool" aria-label="Home">
      <svg width="18" height="16" viewBox="0 0 18 16"><path d="M2 8 L9 2 L16 8 M4 7 V14 H14 V7" fill="none" stroke="#777" stroke-width="1.4"/></svg>
    </span>
    <span class="sep"></span>
    <span class="tool" aria-label="Page">
      <svg width="12" height="16" viewBox="0 0 12 16"><path d="M1.5 1.5 H7.5 L10.5 4.5 V14.5 H1.5 Z" fill="none" stroke="#777" stroke-width="1.4"/></svg>
    </span>
    <span class="sep"></span>
    <span class="tool" aria-label="Sitemap">
      <svg width="18" height="16" viewBox="0 0 18 16"><rect x="6" y="1" width="6" height="4" fill="none" stroke="#777" stroke-width="1.3"/><path d="M9 5 V8 M3 8 H15 M3 8 V10 M15 8 V10" stroke="#777" stroke-width="1.3"/><rect x="1" y="10" width="5" height="4" fill="none" stroke="#777" stroke-width="1.3"/><rect x="12" y="10" width="5" height="4" fill="none" stroke="#777" stroke-width="1.3"/></svg>
    </span>
  </nav>

  <header class="banner">
    <div class="brand"><span>partnerlinkhubgroup</span><span class="mark"></span></div>
    <div class="banner-visual" role="img" aria-label="Illustration of an open business briefcase with papers"></div>
    <div class="tagline">
      <div class="big">INDIVIDUAL</div>
      <div class="small">CUSTOMERS APPROACH</div>
    </div>
    <div class="tag-visual" role="img" aria-label="Illustration of a hanging price tag on a string"></div>
  </header>

  <ul class="side-nav">
    <li><span class="label">Home</span><span class="hint">lorem empus</span></li>
    <li><span class="label">Customer Groups</span><span class="hint">lorem epsum</span></li>
    <li><span class="label">Products</span><span class="hint">lorum epsum</span></li>
    <li><span class="label">Voucher System</span><span class="hint">lerum epsum</span></li>
    <li><span class="label">Contact</span><span class="hint">lerum epsum</span></li>
  </ul>

  <aside class="primary-contact">
    <h3>Primary Contact</h3>
    <strong>The Company Name Inc.</strong><br>
    4120 - 4124 Elm Lane,<br>
    London, BS21 4QT<br>
    <strong>Phone:</strong>&nbsp; +1 800 555 0142
  </aside>

  <div class="photo photo-welcome" role="img" aria-label="Photo of a smiling businesswoman"></div>
  <h1 class="heading welcome-title">Welcome to our Company Website<small>Some words about company</small></h1>
  <p class="copy welcome-copy">Donec et tortor. Praesent iaculis vestibulum neque arcu tortor... fringilla ut, suscipit ac, condimentum sit amet, est. Praesent malesuada purus at dolor. Maecenas porttitor, ante nec pulvinar suscipit, ante nisl lobortis dui, eu malesuada pede tortor mollis wisi. Suspendisse egestas. Quisque enim...</p>
  <span class="more more-welcome"><span class="dot">+</span>read more about company</span>

  <h2 class="heading priority-title">Priority line of business<small>Professional management and researches</small></h2>
  <p class="copy priority-copy">Praesent malesuada purus at dolor. Suspendisse egestas. Quisque enim. Duis neque pede, ultrices sed, vulputate at, vestibulum id, nunc quisque orci quam, consectetuer quis, rhoncus sed...</p>
  <ul class="priority-links">
    <li><span>Praesent malesuada purus at dolor.</span></li>
    <li><span>Suspendisse egestas quisque enim.</span></li>
    <li><span>Duis neque pede ultrices sed vulput</span></li>
    <li><span>Quisque orci quam, consectetuer quis</span></li>
    <li><span>Rhoncus sed vehicula nec velit.</span></li>
  </ul>

  <div class="column-rule"></div>

  <h2 class="heading news-title">Latest News<small>corporate highlights</small></h2>

  <div class="photo photo-news-1" role="img" aria-label="Photo of a smiling woman at the office"></div>
  <p class="news-item news-1"><span class="date">21.05</span>Praesent iaculis vestibulum neque arcu tortor fringilla ut, suscipit ac, condimentum sit...</p>
  <span class="more more-news-1"><span class="dot">+</span>read more</span>

  <div class="news-divider"></div>

  <div class="photo photo-news-2" role="img" aria-label="Photo of a woman talking on the phone"></div>
  <p class="news-item news-2"><span class="date">15.05</span>Praesent male-suada purus at dolor. Maecenas porttitor, ante nec pulvinar suscipit...</p>
  <span class="more more-news-2"><span class="dot">+</span>read more</span>

  <footer class="footer">partnerlinkhubgroup.Com © 2013 | Privacy Policy | Terms Of Use</footer>

</div>
</body>
</html>
```